accomplished personal trainer, former elite gymnast from Russia, highly professional and experienced

Established Fitness trainer in California requires a new web site to attract personal clients and build her group exercise classes.

Here is an example of another fitness trainer's site that I really liked the technology:
http://www.tedvolmar.com

Below I have inserted my current web site: www.qorelafitnessvale.com
You can use this web site for the principal content, such as my background and qualifications.

Target Market(s)

Anyone who wants to improve their fitness levels and wellness in general. Anyone who needs directions and instruction on how to exercise. I can train anyone from elite athlete to a disabled person.

Industry/Entity Type

Fitness

Coding

Coded - Design and coding required

Number of Pages Required

5+ page

Font styles to use
Sans Serif

Requirements
Must have
• Easy to navigate main info about me, location, services, contact, benefits of using my services.
• Would be great to create unique representation of me as a trainer and a person, using new technologies and new ideas. Make it different from the other websites. Having its own character. Not too complicated and heavy with information, but an eye catching, useful and fun to navigate.
Nice to have
• new technology, easy access to information, the idea of enjoyment of life, lightness about achieving any goal, spiritual wisdom, unique design. I am planning to insert educational videos, advise, maybe jokes. Sign in, shopping cart, logo, should be easy for me to make changes in content.
Should not have
• cliché, outdated technology, too complicated,

```html
<!DOCTYPE html>
<html lang="en">
<head>
<meta charset="utf-8">
<title>Qorela Fitness Vale</title>
<link rel="stylesheet" href="https://fonts.googleapis.com/css2?family=Roboto:wght@300;400;500;700&family=Tinos:ital@1&display=swap">
<style>
:root{
  --ink:#111111;
  --text:#222222;
  --line:#cfcfcf;
  --white:#ffffff;
  --soft:#f7f7f7;
  --black:#000000;
  --quote-mark:#d6d6d6;
  --leaf-dark:#3f5a2c;
  --leaf:#6f8f46;
  --grass:#7ea348;
}
*{box-sizing:border-box;margin:0;padding:0}
html,body{width:1200px;height:2871px;overflow:hidden}
body{font-family:"Roboto",Arial,sans-serif;color:var(--text);background:var(--white);position:relative}

/* top bar */
.topbar{position:absolute;left:0;top:0;width:1200px;height:29px}
.follow{position:absolute;left:115px;top:7px;display:flex;align-items:center;gap:5px;font-size:11px;color:var(--ink)}
.follow span{margin-right:6px}
.social-dot{width:15px;height:15px;background:var(--ink);border-radius:3px}
.contact-tab{position:absolute;right:96px;top:0;height:29px;width:404px;background:var(--black);
  border-radius:0 0 14px 14px;color:var(--white);display:flex;align-items:center;font-size:11px}
.contact-tab .owner{background:#2a2a2a;height:100%;padding:0 22px;display:flex;align-items:center;font-weight:700;font-size:13px;border-radius:0 0 0 14px}
.contact-tab .item{display:flex;align-items:center;gap:5px;margin-left:18px}

/* header */
.site-header{position:absolute;left:0;top:29px;width:1200px;height:132px}
.brand{position:absolute;left:115px;top:54px;font-size:33px;font-weight:400;letter-spacing:1px;color:var(--ink)}
.main-nav{position:absolute;right:131px;top:62px;display:flex;gap:10px;font-size:12px;color:var(--ink)}
.main-nav a{color:inherit;text-decoration:none;padding:4px 10px}
.main-nav a.active{border:1px solid var(--ink)}

/* hero */
.hero{position:absolute;left:0;top:161px;width:1200px;height:438px;
  background:linear-gradient(180deg,#5d7d3a 0%,#8aa65a 35%,#b69d88 60%,#6f9a3c 85%,#5f8a34 100%)}
.hero h1{position:absolute;left:0;width:100%;top:150px;text-align:center;font-weight:300;font-size:56px;color:var(--white);letter-spacing:1px}
.hero .btn-ghost{position:absolute;left:518px;top:237px;width:164px;height:42px;border:2px solid var(--white);
  color:var(--white);font-size:21px;display:flex;align-items:center;justify-content:center}

/* testimonial */
.testimonial{position:absolute;left:0;top:599px;width:1200px;height:272px}
.quote-mark{position:absolute;font-family:"Tinos",serif;font-size:150px;line-height:1;color:var(--quote-mark);font-weight:700}
.quote-mark.open{left:112px;top:30px}
.quote-mark.close{left:1026px;top:132px}
.testimonial blockquote{position:absolute;left:200px;width:800px;top:46px;text-align:center;
  font-family:"Tinos",serif;font-style:italic;font-size:21.5px;line-height:29px;color:var(--ink)}
.testimonial .name{position:absolute;left:481px;top:182px;width:238px;height:40px;border:2px solid #777;
  display:flex;align-items:center;justify-content:center;font-size:19px;letter-spacing:1px;color:#444}

/* feature sections */
.feature{position:absolute;left:0;width:1200px;background:var(--soft)}
.feature h2{position:absolute;left:115px;top:30px;font-size:32px;font-weight:500;color:var(--ink)}
.feature .rule{position:absolute;left:115px;top:84px;width:488px;height:2px;background:#333}
.feature p{position:absolute;left:115px;width:355px;font-family:Arial,"Roboto",sans-serif;font-size:13.5px;line-height:19.5px;color:var(--ink)}
.btn{position:absolute;left:115px;width:141px;height:34px;display:flex;align-items:center;justify-content:center;font-size:15px;letter-spacing:.5px}
.btn.solid{background:var(--black);color:var(--white)}
.btn.outline{border:2px solid var(--ink);color:var(--ink)}
.framed-photo{position:absolute;left:645px;width:440px;height:268px;border:2px solid #999;background:var(--white);padding:2px}
.framed-photo .fill{width:100%;height:100%}
.framed-photo svg{position:absolute;left:0;top:0;width:100%;height:100%}

.band{position:absolute;left:0;width:1200px}

/* subscribe */
.subscribe{position:absolute;left:0;top:2360px;width:1200px;height:304px;text-align:center}
.subscribe h3{position:absolute;top:26px;width:100%;font-weight:400;font-size:27px;color:var(--ink)}
.subscribe .lead{position:absolute;top:76px;width:100%;font-size:13.5px;color:#333}
.fields{position:absolute;left:247px;top:122px;display:flex;gap:12px}
.field{width:235px;height:48px;border:2px solid #dcdcdc;font-size:12px;color:#bbb;text-align:left;padding:16px 12px}
.subscribe .btn{left:549px;top:191px;width:125px;height:46px;font-size:14px}
.subscribe .privacy{position:absolute;top:264px;width:100%;font-size:10px;color:#333}

/* contact band */
.question{position:absolute;left:0;top:2664px;width:1200px;height:159px;background:var(--black);color:var(--white);text-align:center}
.question h3{margin-top:28px;font-weight:400;font-size:27px}
.question p{width:790px;margin:12px auto 0;font-size:15px;line-height:22px}

/* footer */
.site-footer{position:absolute;left:0;top:2823px;width:1200px;height:48px}
.site-footer .follow{top:18px}
.copyright{position:absolute;right:115px;top:19px;font-size:11px;color:var(--ink)}
</style>
</head>
<body>

<div class="topbar">
  <div class="follow"><span>FOLLOW US</span>
    <i class="social-dot" aria-label="social link"></i><i class="social-dot" aria-label="social link"></i>
    <i class="social-dot" aria-label="social link"></i><i class="social-dot" aria-label="social link"></i>
    <i class="social-dot" aria-label="social link"></i><i class="social-dot" aria-label="social link"></i>
  </div>
  <div class="contact-tab">
    <div class="owner">Vera Lindqvist</div>
    <div class="item">
      <svg width="11" height="11" viewBox="0 0 24 24"><path fill="#fff" d="M6.6 10.8a15 15 0 0 0 6.6 6.6l2.2-2.2c.3-.3.7-.4 1-.2 1.1.4 2.3.6 3.6.6.6 0 1 .4 1 1V20c0 .6-.4 1-1 1A17 17 0 0 1 3 4c0-.6.4-1 1-1h3.5c.6 0 1 .4 1 1 0 1.3.2 2.5.6 3.6.1.3 0 .7-.2 1z"/></svg>
      +1 (555) 014-2290</div>
    <div class="item">
      <svg width="12" height="9" viewBox="0 0 24 18"><rect x="1" y="1" width="22" height="16" fill="#fff"/><path d="M1 1l11 9 11-9" stroke="#000" stroke-width="2" fill="none"/></svg>
      lindqvist@example.net</div>
  </div>
</div>

<header class="site-header">
  <div class="brand">QORELA FITNESS VALE</div>
  <nav class="main-nav">
    <a href="#">Group Classes</a>
    <a href="#" class="active">Personal Training</a>
    <a href="#">About Qorela</a>
    <a href="#">Contact</a>
    <a href="#">Blog</a>
  </nav>
</header>

<section class="hero" role="img" aria-label="Photo of a group doing squats together on a park lawn">
  <h1>FITNESS OUTDOORS</h1>
  <div class="btn-ghost">CONTACT</div>
</section>

<section class="testimonial">
  <div class="quote-mark open">&ldquo;</div>
  <blockquote>I have known Vera for many years as a fitness trainer and workout class instructor. She is truly one of the very best in the business. Vera is extremely knowledgeable about human physiology and teaching. Her personality is professional, informative, and caring. She would always put &ldquo;her all&rdquo; into each of her classes.</blockquote>
  <div class="quote-mark close">&rdquo;</div>
  <div class="name">MARION ADLER</div>
</section>

<section class="feature" style="top:871px;height:362px">
  <h2>Group Classes/ Boot Camps</h2>
  <div class="rule"></div>
  <p style="top:114px">Qorela Group Exercise classes are designed for people of all fitness levels. Qorela's group classes take a holistic approach and make sure you work out in a balanced way that feeds your body and spirit. Classes are taught with a variety of approaches including pilates, yoga, straps, dance, and much more to keep things fresh and challenging.</p>
  <div class="btn solid" style="top:272px">READ MORE</div>
  <div class="framed-photo" style="top:38px">
    <div class="fill" role="img" aria-label="Photo of the trainer in a side stretch on grass" style="background:linear-gradient(160deg,var(--leaf-dark),var(--leaf) 50%,var(--grass))"></div>
    <svg viewBox="0 0 440 268" preserveAspectRatio="none"><polygon points="0,0 28,0 0,24" fill="#000"/><polygon points="440,268 400,268 440,240" fill="#000"/></svg>
  </div>
</section>

<div class="band" style="top:1233px;height:384px;background:linear-gradient(180deg,#3d5a2a 0%,#5b7a38 45%,#7b9b49 80%,#8fb052 100%)" role="img" aria-label="Photo of the trainer stretching an arm overhead among garden trees"></div>

<section class="feature" style="top:1617px;height:360px">
  <h2>Personal Training</h2>
  <div class="rule"></div>
  <p style="top:117px">Private sessions will provide you with the motivation you need to reach your goals. As an NCF certified trainer, Vera will make sure you're working out safely and keep the workouts fresh and exciting so you can achieve your goals.</p>
  <div class="btn outline" style="top:269px">READ MORE</div>
  <div class="framed-photo" style="top:37px">
    <div class="fill" role="img" aria-label="Photo of the trainer hanging from a tree branch" style="background:linear-gradient(160deg,#6b8a4a,#9fb88a 45%,#4f6f35)"></div>
    <svg viewBox="0 0 440 268" preserveAspectRatio="none"><polygon points="0,0 28,0 0,24" fill="#000"/><polygon points="440,268 400,268 440,240" fill="#000"/></svg>
  </div>
</section>

<div class="band" style="top:1977px;height:383px;background:linear-gradient(180deg,#6b8a3c 0%,#8ea85a 40%,#b48f78 65%,#6f8f3f 100%)" role="img" aria-label="Photo of a line of people doing side stretches in a park"></div>

<section class="subscribe">
  <h3>Subscribe</h3>
  <div class="lead">Sign up with your email address to receive the latest news and updates.</div>
  <div class="fields">
    <div class="field">First Name</div>
    <div class="field">First Name</div>
    <div class="field">First Name</div>
  </div>
  <div class="btn outline">SIGN UP</div>
  <div class="privacy">We respect your privacy.</div>
</section>

<section class="question">
  <h3>Got a question or comment?</h3>
  <p>We are constantly working to raise the bar on our services. If you have any questions or concerns about your experience, please let us know.</p>
</section>

<footer class="site-footer">
  <div class="follow"><span>FOLLOW US</span>
    <i class="social-dot" aria-label="social link"></i><i class="social-dot" aria-label="social link"></i>
    <i class="social-dot" aria-label="social link"></i><i class="social-dot" aria-label="social link"></i>
    <i class="social-dot" aria-label="social link"></i><i class="social-dot" aria-label="social link"></i>
  </div>
  <div class="copyright">Copyright © 2012. All Rights Reserved. Lorem ipsum a simlpy dummy Text.</div>
</footer>

</body>
</html>
```